Construction company looking for modern

**Tallow Crest Joinery Limited**

We need a website for a renovation/remodeling company based in Hamilton, New Zealand. Ideally it will catch clients' attention and be modern and professional looking. I have attached a logo that I have just recently had made (through PixelHarbor). If the website could reflect this style and colour schemes, that would be awesome. The final design should communicate a trustworthiness and professionalism.

I have attached photos of a website that I really think is great, so if we could have something that follows along those likes,

https://www.dailyplover.example/local-news/news/local-builder-named-top-apprentice-for-region/QZTRPLA8VXN2MJ5DFYUEKHSWGO/

I won a competition a few years ago while I was an apprentice, If we could somehow put that in there as one of my achievements to try to bring in some trust that would be awesome. I would like to add a new picture though because my beard in that photo is wild.

Target Market(s)

Families that want live in the homes that i'm working on. not investors. People that are looking for quality not cheapest price.

Industry/Entity Type

Construction, Home renovations, Maintenance, Deck Builds, New Builds, Bathrooms, Kitchens

Coding

Coded - Design and coding required

Number of Pages Required

5+ page

Font styles to use
Sans Serif

Colors
6B429C
8869AF
B7A5CE
E3DAEB
F3F0F8

Requirements
Must have
• Contact us page, large clear pictures, Colours the work with the purple in my logo. That will be my company colour so I'm thinking black and purple, or what ever compliments purple nicely
Nice to have
• Page for Renovations, Testimonials, Contact us, Home, About us
Should not have
• Plain looking pages, empty white space, I want the text to be beside a nice big picture etc

```html
<!DOCTYPE html>
<html lang="en">
<head>
<meta charset="utf-8">
<title>Tallow Crest Joinery – Home</title>
<link href="https://fonts.googleapis.com/css2?family=Work+Sans:ital,wght@0,400;0,500;0,600;1,400&display=swap" rel="stylesheet">
<style>
:root{
  --purple:#6B429C;
  --purple-mid:#8869AF;
  --purple-soft:#B7A5CE;
  --lilac:#E3DAEB;
  --mist:#F3F0F8;
  --ink:#222222;
  --dark:#333333;
  --dark-btn:#2b2b2b;
  --white:#ffffff;
  --gold:#e8a43a;
}
*{margin:0;padding:0;box-sizing:border-box}
html,body{width:1200px;height:3450px;overflow:hidden}
body{position:relative;font-family:"Work Sans",sans-serif;color:var(--ink);background:var(--white)}
.abs{position:absolute}
a{color:inherit;text-decoration:none}

/* header */
.site-header{left:0;top:0;width:1200px;height:74px;background:var(--white)}
.brand{left:201px;top:20px;display:flex;align-items:center;gap:8px;color:var(--purple);font-weight:600;font-size:13px;line-height:1.1;width:130px}
.brand-mark{width:14px;height:14px;background:var(--purple);flex:none}
.nav{top:30px;font-size:11px;font-weight:500;color:var(--ink)}
.nav.active{color:var(--purple)}
.nav-phone{left:767px;top:30px;font-size:11px;color:var(--purple);display:flex;align-items:center;gap:6px}
.btn{display:flex;align-items:center;justify-content:center;font-size:11px;font-weight:600}
.btn-purple{background:var(--purple);color:var(--white)}
.btn-dark{background:var(--dark-btn);color:var(--white)}
.btn-outline{border:2px solid var(--purple);color:var(--purple);background:transparent}

/* photo areas */
.photo{position:absolute}
.photo-living{left:0;top:74px;width:1200px;height:600px;
  background:
    linear-gradient(180deg,rgba(40,34,28,.10) 0%,rgba(40,34,28,0) 30%,rgba(60,50,40,.25) 100%),
    linear-gradient(90deg,#5f5850 0%,#7d766c 12%,#a49c90 26%,#d6d2ca 44%,#e4e1da 52%,#bdb5a8 66%,#8f8678 80%,#6a6156 92%,#c9c2b6 100%)}
.photo-kitchen{left:0;top:1055px;width:999px;height:581px;
  background:
    linear-gradient(180deg,rgba(255,255,255,.0) 0%,rgba(150,148,144,.35) 75%,rgba(120,118,114,.55) 100%),
    linear-gradient(90deg,#cfccc7 0%,#4d5a45 9%,#3c4a36 18%,#e9e7e3 26%,#f4f3f1 48%,#dedbd6 70%,#b9b6b1 86%,#d8d5d0 100%)}
.photo-bath{left:457px;top:1650px;width:743px;height:436px;
  background:
    linear-gradient(180deg,rgba(255,255,255,0) 70%,rgba(200,180,150,.35) 100%),
    linear-gradient(90deg,#c79a62 0%,#d9b98a 6%,#efe8de 12%,#f5f1ea 45%,#caa06a 53%,#dbb582 62%,#f1ede6 72%,#5f8a45 82%,#3f6a2e 100%)}
.photo-kitchen-two{left:0;top:1982px;width:443px;height:491px;
  background:
    linear-gradient(180deg,rgba(255,255,255,0) 55%,rgba(170,160,150,.35) 100%),
    linear-gradient(90deg,#e2ded8 0%,#c69b63 15%,#b98a55 28%,#f1eeea 42%,#e8e5e0 60%,#c08f5a 74%,#f0ede8 88%,#d8d4ce 100%)}
.photo-lounge{left:457px;top:2100px;width:743px;height:373px;
  background:
    linear-gradient(180deg,rgba(255,255,255,0) 55%,rgba(120,120,120,.35) 100%),
    linear-gradient(90deg,#d9d7d4 0%,#f0c22e 18%,#a7a7a6 28%,#e5e4e2 42%,#77787a 52%,#eeedeb 64%,#3d3d3f 78%,#f2f1ef 90%,#dcdad6 100%)}

/* hero */
.hero-title{left:201px;top:258px;width:640px;font-size:45px;line-height:54px;font-weight:600;color:var(--white);letter-spacing:1px;text-shadow:0 1px 6px rgba(0,0,0,.25)}
.hero-dots span{position:absolute;left:988px;width:8px;height:8px;border-radius:50%;background:var(--white)}

/* welcome */
.welcome{left:0;top:674px;width:1200px;height:381px;background:var(--purple);color:var(--white);text-align:center}
.eyebrow{font-size:18px;font-weight:600}
.section-title{font-size:37px;font-weight:400;letter-spacing:1px}
.welcome p{position:absolute;left:280px;top:178px;width:640px;font-size:13.5px;line-height:20.5px}

/* renovations */
.reno-card{left:743px;top:1131px;width:394px;height:430px;background:var(--mist)}
.label{font-size:14px;font-weight:600;color:var(--purple)}
.card-title{font-size:24px;line-height:30px;font-weight:400;color:var(--ink);letter-spacing:.4px}
.small-copy{font-size:11px;line-height:17px;color:var(--ink)}

/* projects */
.projects-intro{left:0;top:1636px;width:443px;height:332px;background:var(--mist)}
.caption{left:0;top:2357px;width:443px;height:116px;background:rgba(243,240,248,.92)}
.circle-btn{border:1px solid var(--purple);border-radius:50%;display:flex;align-items:center;justify-content:center}

/* testimonials */
.testimonials{left:0;top:2473px;width:1200px;height:600px;background:linear-gradient(180deg,#7550a6,#6d449e);color:var(--white);text-align:center}
.frame{border:1px solid rgba(255,255,255,.75)}
.quote{left:305px;top:288px;width:590px;font-style:italic;font-size:14.5px;line-height:20px}
.arrow-circle{width:36px;height:36px;border:1px solid rgba(255,255,255,.8);border-radius:50%;background:var(--purple);display:flex;align-items:center;justify-content:center}

/* footer */
.footer{left:0;top:3073px;width:1200px;height:377px;background:var(--dark);color:var(--white)}
.footer h4{font-size:14px;font-weight:500;color:var(--purple-mid)}
.footer .item{font-size:11px;line-height:14px;color:var(--white)}
.social span{position:absolute;width:30px;height:30px;border-radius:50%;background:var(--purple-soft)}
.social span.on{background:var(--purple)}
.legal{left:200px;top:3356px;font-size:11px;color:var(--white)}
.legal em{font-style:normal;color:var(--purple-mid)}
</style>
</head>
<body>

<header class="abs site-header">
  <div class="abs brand"><span class="brand-mark"></span>Tallow Crest Joinery</div>
  <a class="abs nav active" style="left:426px">-- Home --</a>
  <a class="abs nav" style="left:509px">About Us</a>
  <a class="abs nav" style="left:584px">Renovations</a>
  <a class="abs nav" style="left:674px">Testimonials</a>
  <div class="abs nav-phone">
    <svg width="10" height="10" viewBox="0 0 24 24"><path d="M6.6 10.8a15 15 0 006.6 6.6l2.2-2.2a1 1 0 011-.25 11.4 11.4 0 003.6.6 1 1 0 011 1V20a1 1 0 01-1 1A17 17 0 013 4a1 1 0 011-1h3.5a1 1 0 011 1c0 1.25.2 2.45.6 3.6a1 1 0 01-.25 1z" fill="#6B429C"/></svg>
    027 418 6620
  </div>
  <a class="abs btn btn-purple" style="left:887px;top:19px;width:113px;height:36px">Contact Us</a>
</header>

<div class="photo photo-living" role="img" aria-label="Bright open-plan living room with grey sofa, armchair, timber floor and bookshelves"></div>
<h1 class="abs hero-title">We’re an independent family-owned, new home building company</h1>
<a class="abs btn btn-purple" style="left:200px;top:450px;width:112px;height:36px">Contact Us</a>
<svg class="abs" style="left:242px;top:608px" width="28" height="16" viewBox="0 0 28 16"><path d="M2 2l12 12L26 2" fill="none" stroke="#fff" stroke-width="2"/></svg>
<div class="abs hero-dots"><span style="top:315px"></span><span style="top:336px"></span><span style="top:357px"></span></div>

<section class="abs welcome">
  <div class="abs eyebrow" style="left:0;top:74px;width:1200px">Welcome to</div>
  <h2 class="abs section-title" style="left:0;top:104px;width:1200px">Tallow Crest Joinery</h2>
  <p>There are many variations of passages of Lorem Ipsum available, but the majority have suffered alteration in some form, by injected humour, or randomised words which don't look even slightly believable. If you are going to use a passage of Lorem Ipsum,</p>
  <a class="abs btn btn-dark" style="left:544px;top:267px;width:112px;height:38px">Explore More</a>
</section>

<div class="photo photo-kitchen" role="img" aria-label="White modern kitchen with island, tufted bar stools and garden window"></div>
<div class="abs reno-card">
  <div class="abs label" style="left:38px;top:60px">Renovations</div>
  <h3 class="abs card-title" style="left:38px;top:93px;width:330px">Bathroom, kitchens &amp; general home renovations made easy.</h3>
  <p class="abs small-copy" style="left:38px;top:211px;width:320px">There are many variations of passages of Lorem Ipsum available, but the majority have suffered alteration in some form, by injected humour, or randomised words which don't look even slightly believable. If you are going to use a passage of Lorem Ipsum,</p>
  <a class="abs btn btn-outline" style="left:38px;top:333px;width:112px;height:36px">Discover More</a>
</div>

<section class="abs projects-intro">
  <div class="abs label" style="left:63px;top:76px">Recent Projects</div>
  <h3 class="abs card-title" style="left:63px;top:112px;width:330px">Completed renovation/ remodeling in hamilton, new zealand</h3>
  <a class="abs btn btn-outline" style="left:63px;top:219px;width:111px;height:36px">View All</a>
</section>
<div class="photo photo-bath" role="img" aria-label="Bathroom with timber slat wall, twin round mirrors and freestanding bath beside a garden"></div>
<div class="photo photo-kitchen-two" role="img" aria-label="Bright kitchen with pendant lights, timber range hood and flowers"></div>
<div class="abs caption">
  <div class="abs" style="left:63px;top:36px;font-size:17px;font-weight:500">Lorem Ipsum is simply</div>
  <div class="abs" style="left:63px;top:63px;font-size:12px;color:var(--purple)">Kitchens Renovation</div>
  <div class="abs circle-btn" style="left:341px;top:40px;width:40px;height:40px">
    <svg width="10" height="8" viewBox="0 0 10 8"><path d="M0 4h9M6 1l3 3-3 3" fill="none" stroke="#6B429C"/></svg>
  </div>
</div>
<div class="photo photo-lounge" role="img" aria-label="Living room with grey sofa, yellow cushions, patterned rug and wall-mounted TV"></div>

<section class="abs testimonials">
  <div class="abs eyebrow" style="left:0;top:74px;width:1200px">Testimonials</div>
  <h2 class="abs section-title" style="left:0;top:108px;width:1200px">Happy clients say</h2>
  <div class="abs frame" style="left:200px;top:184px;width:800px;height:274px"></div>
  <div class="abs frame" style="left:210px;top:194px;width:780px;height:254px"></div>
  <svg class="abs" style="left:580px;top:230px" width="40" height="30" viewBox="0 0 40 30"><path d="M2 28c0-14 5-22 14-26M4 28c3-3 9-3 9 1M22 28c0-14 5-22 14-26M24 28c3-3 9-3 9 1" fill="none" stroke="#e8a43a" stroke-width="2"/></svg>
  <p class="abs quote">" Sed ut perspiciatis unde omnis iste natus error sit voluptatem accusantium doloremque laudantium, totam rem aperiam, eaque ipsa quae ab illo inventore veritatis et quasi architecto beatae vitae dicta sunt explicabo. Nemo enim ipsam voluptatem quia voluptas sit."</p>
  <div class="abs" style="left:0;top:378px;width:1200px;font-size:14px;font-weight:500">- M. Ellery -</div>
  <div class="abs" style="left:0;top:400px;width:1200px;font-size:12px;color:var(--gold);letter-spacing:2px">★★★★★</div>
  <div class="abs arrow-circle" style="left:187px;top:302px"><svg width="10" height="8" viewBox="0 0 10 8"><path d="M10 4H1M4 1L1 4l3 3" fill="none" stroke="#fff"/></svg></div>
  <div class="abs arrow-circle" style="left:975px;top:302px"><svg width="10" height="8" viewBox="0 0 10 8"><path d="M0 4h9M6 1l3 3-3 3" fill="none" stroke="#fff"/></svg></div>
  <a class="abs btn btn-dark" style="left:544px;top:490px;width:112px;height:37px">View All</a>
</section>

<footer class="abs footer">
  <div class="abs" style="left:225px;top:76px;width:117px;height:117px;background:#fff;transform:rotate(45deg)"></div>
  <div class="abs" style="left:226px;top:120px;width:114px;text-align:center;font-size:13px;font-weight:600;line-height:15px;color:var(--purple)">Tallow Crest Joinery</div>

  <h4 class="abs" style="left:406px;top:73px">Contact Us</h4>
  <svg class="abs" style="left:406px;top:112px" width="10" height="10" viewBox="0 0 24 24"><path d="M6.6 10.8a15 15 0 006.6 6.6l2.2-2.2a1 1 0 011-.25 11.4 11.4 0 003.6.6 1 1 0 011 1V20a1 1 0 01-1 1A17 17 0 013 4a1 1 0 011-1h3.5a1 1 0 011 1c0 1.25.2 2.45.6 3.6a1 1 0 01-.25 1z" fill="#8869AF"/></svg>
  <div class="abs item" style="left:431px;top:110px;font-size:14px">(07) 555 0148</div>
  <svg class="abs" style="left:406px;top:144px" width="10" height="10" viewBox="0 0 10 10"><path d="M0 5L5 1l5 4v5H0z" fill="#8869AF"/></svg>
  <div class="abs item" style="left:431px;top:143px">info@tallowcrestjoinery.example</div>
  <svg class="abs" style="left:406px;top:175px" width="10" height="12" viewBox="0 0 10 12"><path d="M5 12S0 7 0 4.5a5 5 0 0110 0C10 7 5 12 5 12z" fill="#8869AF"/><circle cx="5" cy="4.5" r="1.7" fill="#333"/></svg>
  <div class="abs item" style="left:431px;top:174px;width:170px;line-height:18px">Tallow Crest Joinery<br>118 Kowhai Bend Road,<br>Fernhill 3204</div>

  <h4 class="abs" style="left:649px;top:73px">Quick Links</h4>
  <div class="abs item" style="left:649px;top:110px;line-height:22.5px">Home<br>About Us<br>Renovations<br>Testimonials<br>Contact Us</div>

  <h4 class="abs" style="left:818px;top:73px">Office Hours</h4>
  <div class="abs item" style="left:818px;top:110px">Monday - Friday: 9am - 4pm</div>
  <div class="abs social" style="left:0;top:0"><span style="left:819px;top:144px"></span><span class="on" style="left:857px;top:144px"></span><span style="left:894px;top:144px"></span></div>

  <div class="abs" style="left:933px;top:268px;width:68px;height:68px;border-radius:50%;background:#d9e6b8"></div>
</footer>
<div class="abs legal">© 2023 - <em>Tallow Crest Joinery</em>. All rights reserved &nbsp;&nbsp;&nbsp; | &nbsp;&nbsp;&nbsp; Privacy policy &nbsp;&nbsp;&nbsp; | &nbsp;&nbsp;&nbsp; Terms and conditions</div>

</body>
</html>
```